We have a menu to be designed with an "old school" diner theme. There will be a total of 10 pages including a full color cover.
Looking for several "looks" to present the owner, so if you have a few ideas for concepts...please include them. Need at least the cover and 1-3 interior pages to present before completing the entire 10 pages.
We would like to have the concepts available to present on Tuesday August 27th if possible.
Once a concept is chosen, we will need all 10 pages setup and ready to print. We will need the final design sent to us in an editable file (InDesign is preferred).
Size: 8.5" wide by 14" high
Color: Full color with 1/8" bleeds
We are providing the current menu for text of menu items only...not for layout.
Please do NOT use leaders ( ..............4.99) in front of prices and do NOT use dollar sign symbols ($). Please insert the prices at the end of each description with 2 spaces before the price. See below for an example:
____________________________________
Tuna
Freshly made tuna mixed with celery
and Brackley’s mayo (no onion) and
with lettuce 7.29
Please use an easily legible font for the descriptions and something a little more bold for the item names.
Please follow the order of the items as they are on the attached PDF.
You can see what they currently have on their website:
http://www.copperkettlegrill.example/
Updates
My apologies for not getting that PDF and logo uploaded. I thought it had been submitted.
They are both uploaded now.
Thanks!
Really need to try to get the concepts in asap to show our client. Thanks!
Thank you all for submitting the designs. We would like to see some different looks for the inside pages. Lots of covers have been submitted, but not very many inside pages. Please send a sample or two as soon as possible. We would like to choose a design soon.
Thank you!
Diner

```html
<!DOCTYPE html>
<html lang="en">
<head>
<meta charset="utf-8">
<title>Copper Kettle Grill – Breakfast Menu</title>
<link rel="stylesheet" href="https://fonts.googleapis.com/css2?family=Roboto+Condensed:wght@300;400;700&family=Oswald:wght@500&display=swap">
<style>
  :root {
    --ink-blue: #2b8bcc;
    --ribbon-blue: #3a9ad9;
    --ribbon-shade: #2a7fbd;
    --ribbon-fold: #1d5f8f;
    --price-red: #e53a3f;
    --rule-blue: #86c6ea;
    --paper: #ffffff;
  }
  * { margin: 0; padding: 0; box-sizing: border-box; }
  html, body { width: 736px; height: 1200px; overflow: hidden; background: var(--paper); }
  .menu-page {
    position: relative; width: 736px; height: 1200px;
    font-family: "Roboto Condensed", "Arial Narrow", sans-serif;
  }
  .brand-name {
    position: absolute; top: 104px; left: 0; width: 736px;
    text-align: center; font-size: 34px; font-weight: 700;
    color: var(--price-red); letter-spacing: 0.5px;
  }
  .ribbon { position: absolute; top: 234px; left: 203px; }
  .ribbon-title {
    position: absolute; top: 239px; left: 0; width: 736px; text-align: center;
    font-family: "Oswald", "Arial Narrow", sans-serif; font-weight: 500;
    font-size: 38px; line-height: 52px; color: #fff;
  }
  .extras-note {
    position: absolute; top: 294px; width: 736px; text-align: center;
    font-size: 12px; color: var(--price-red);
  }
  .section { position: absolute; left: 126px; width: 479px; }
  .section-title {
    text-align: center; font-weight: 300; font-size: 30px; line-height: 36px;
    color: var(--price-red); padding-bottom: 2px;
    border-bottom: 1px solid var(--rule-blue);
  }
  .item-list { list-style: none; margin-top: 5px; }
  .item { font-size: 15px; line-height: 22.4px; white-space: nowrap; }
  .item-name { font-weight: 700; color: var(--ink-blue); }
  .price { font-weight: 400; color: var(--price-red); margin-left: 4px; }
  .size-label { font-weight: 700; color: var(--ink-blue); margin-left: 30px; }
  .size-label + .price { margin-left: 4px; }
  .price + .size-label { margin-left: 34px; }
  .two-columns { display: flex; }
  .two-columns .item-list:first-child { width: 275px; }
  .serving-note {
    margin-top: 10px; text-align: center; font-size: 9px; color: var(--price-red);
  }
</style>
</head>
<body>
<main class="menu-page">
  <div class="brand-name">Copper Kettle Grill</div>

  <svg class="ribbon" width="330" height="62" viewBox="0 0 330 62" aria-hidden="true">
    <polygon points="0,12 40,12 40,58 0,58 16,35" fill="var(--ribbon-shade)"/>
    <polygon points="330,12 290,12 290,58 330,58 314,35" fill="var(--ribbon-shade)"/>
    <polygon points="34,52 40,58 40,52" fill="var(--ribbon-fold)"/>
    <polygon points="296,52 290,58 290,52" fill="var(--ribbon-fold)"/>
    <rect x="34" y="3" width="262" height="49" fill="var(--ribbon-blue)"/>
  </svg>
  <h1 class="ribbon-title">Breakfast</h1>
  <p class="extras-note">Extra: .75-whites.75</p>

  <section class="section egg-specialties" style="top:318px">
    <h2 class="section-title">Egg Specialties</h2>
    <div class="two-columns">
      <ul class="item-list">
        <li class="item"><span class="item-name">Two eggs any style</span><span class="price">4.49</span></li>
        <li class="item"><span class="item-name">With bacon or sausage</span><span class="price">5.29</span></li>
        <li class="item"><span class="item-name">With ham steak</span><span class="price">5.99</span></li>
        <li class="item"><span class="item-name">With Country Fried Steak</span><span class="price">7.99</span></li>
        <li class="item"><span class="item-name">Diced ham and scrambled eggs</span><span class="price">5.59</span></li>
      </ul>
      <ul class="item-list">
        <li class="item"><span class="item-name">Smoked Sausage and eggs</span><span class="price">6.79</span></li>
        <li class="item"><span class="item-name">Corned beef hash and eggs</span><span class="price">7.29</span></li>
        <li class="item"><span class="item-name">Chopped steak and eggs</span><span class="price">7.29</span></li>
        <li class="item"><span class="item-name">N.Y. Strip steak and eggs</span><span class="price">9.29</span></li>
      </ul>
    </div>
    <p class="serving-note">Above items served with home fries, hash browns, grits, oatmeal or sliced tomato and toast, bagel, biscuit or English muffin</p>
  </section>

  <section class="section house-specialities" style="top:522px">
    <h2 class="section-title">House Specialities</h2>
    <ul class="item-list">
      <li class="item"><span class="item-name">Low Carb Breakfast Plate (3 eggs w/choice of bacon, sausage or ham)</span><span class="price">6.49</span></li>
      <li class="item"><span class="item-name">Lox Platter (includes tomato, onion, cream cheese and bagel)</span><span class="price">8.99</span></li>
      <li class="item"><span class="item-name">Biscuits and homemade sausage gravy</span><span class="price">5.99</span></li>
      <li class="item"><span class="item-name">2-2-2: 2 eggs, 2 pancakes, 2 links, or 2 bacon</span><span class="price">6.79</span></li>
      <li class="item"><span class="item-name">Farmer’s special: 1 French toast, 1 egg, 2 links, or 2 bacon</span><span class="price">6.59</span></li>
    </ul>
  </section>

  <section class="section sides" style="top:701px">
    <h2 class="section-title">Sides</h2>
    <ul class="item-list">
      <li class="item"><span class="item-name">Toast or buttermilk biscuit</span><span class="price">1.75</span></li>
      <li class="item"><span class="item-name">Bagel with butter</span><span class="price">1.75</span></li>
      <li class="item"><span class="item-name">Bagel with cream cheese</span><span class="price">2.10</span></li>
      <li class="item"><span class="item-name">Bagel with cream cheese spreads (lox, chives or vegetable)</span><span class="price">2.85</span></li>
      <li class="item"><span class="item-name">English muffin</span><span class="price">1.75</span></li>
      <li class="item"><span class="item-name">Assorted muffins</span><span class="price">2.55</span></li>
      <li class="item"><span class="item-name">Hot butter croissant</span><span class="price">2.75</span></li>
      <li class="item"><span class="item-name">Fresh fruit bowl</span><span class="price">4.50</span></li>
      <li class="item"><span class="item-name">Grits or oatmeal</span><span class="size-label">(cup)</span><span class="price">1.30</span><span class="size-label">(bowl)</span><span class="price">1.95</span></li>
      <li class="item"><span class="item-name">Side of bacon, or sausage</span><span class="price">2.99</span></li>
      <li class="item"><span class="item-name">Side of ham steak</span><span class="price">3.49</span></li>
      <li class="item"><span class="item-name">Turkey Sausage</span><span class="price">3.49</span></li>
      <li class="item"><span class="item-name">Extra egg</span><span class="size-label">(one)</span><span class="price">1.25</span><span class="size-label">(two)</span><span class="price">1.95</span></li>
      <li class="item"><span class="item-name">Side of sausage gravy or s.o.s gravy</span><span class="price">2.25</span></li>
      <li class="item"><span class="item-name">Home fries or hash browns</span><span class="price">1.95</span></li>
      <li class="item"><span class="item-name">Assorted cold cereals</span><span class="price">1.95</span></li>
      <li class="item"><span class="item-name">With banana or raisins</span><span class="price">2.50</span></li>
    </ul>
  </section>
</main>
</body>
</html>
```